quendix.com redesign

We are a successful web hosting company that has been around since 1999 with 10,000 customers managing 2,000 websites and 12,000 domain names. Our challenge - we are losing ground because our site is getting old, our pricing is not competitive and our feature set needs to change to match the new world of mobile centric everything. We want to reach out to all of the domain names that we don't host websites for. We believe that if we designed a new site that focuses on bringing home all of those externally hosted websites to our own web hosting company that we would have a solid future. We need to compete against zelmorix.com, pellwarden.com, grumlane.com, birvon.com, olvestra.com, trekmoss.com, vandrift.com, nulvo.com and 100,000 others. We need to simplify our message with clean design, focused pages, easy decision making processes for the consumer. We use WHMCS for the background provisioning and billing so we can pretty much manage any kind of pricing model and discounted promotion packages.
I would prefer Twitter bootstrap CSS based responsive design.

Reason: I was away on vacation for 2 weeks - I just got back - I need time to fairly review all submissions - thank you for your patience. Tobin Farrow Quendix.com

Thanks to all who submitted sample designs - unfortunately most of them were nothing much more than already available templates with some of my current content and logo added to them. I will try to be more specific to reduce the number of choices. I need the template be fully compatible with WHMCS and Wordpress if you can't make it work with WHMCS directly. Another question I have to ask is -"exactly what am I getting for my $500.00 - is it just a PSD template or actual integration of that theme into WHMCS or Wordpress?"  I don't expect anyone to create new content for the site at that price. What do you charge if  you are able to create content or get directly involved in the site implementation of that template?

```html
<!DOCTYPE html>
<html lang="en">
<head>
<meta charset="utf-8">
<title>Quendix — Web Hosting</title>
<link rel="stylesheet" href="https://fonts.googleapis.com/css2?family=Open+Sans:wght@400;600;700&family=Arimo:wght@400;700&family=PT+Serif:ital,wght@1,700&display=swap">
<style>
:root{
  --navy:#0c3b93;
  --blue:#1a4fa8;
  --blue-bright:#1858c2;
  --ink:#222;
  --muted:#7a7a7a;
  --band:#f2f2f2;
  --card-gray:#d9d9d9;
  --dark:#2b2b2b;
  --black:#111;
  --white:#fff;
}
*{box-sizing:border-box;margin:0;padding:0}
html,body{width:1200px;height:2655px;overflow:hidden;background:var(--white)}
body{font-family:"Open Sans",Arial,sans-serif;color:var(--ink);position:relative}
.abs{position:absolute}

/* top bar */
.topbar{left:0;top:0;width:1200px;height:51px;background:var(--navy)}
.topnav{left:141px;top:0;height:51px;display:flex;gap:20px;align-items:center;color:var(--white);font-size:12.5px}
.topnav span::after{content:"";display:inline-block;margin-left:5px;border:4px solid transparent;border-top-color:var(--white);vertical-align:-2px}
.social{display:flex;gap:9px}
.social i{display:block;width:36px;height:36px;border:2px solid var(--white);border-radius:50%}
.topbar .social{position:absolute;left:873px;top:8px}

/* header */
.brand{left:131px;top:68px;font-size:56px;font-weight:700;color:var(--navy);letter-spacing:-1px;line-height:1}
.mainnav{left:446px;top:90px;display:flex;gap:32px;font-size:13.5px;color:var(--navy)}

/* hero */
.hero{left:131px;top:145px;width:940px;height:430px;background:linear-gradient(120deg,#e7ecf3 0%,#c9d3e0 30%,#4b607e 55%,#c2ccd9 75%,#eef1f5 100%)}
.hero-title{left:0;top:76px;width:940px;padding-left:160px;text-align:center;color:var(--white);font-size:23px;font-weight:400}
.hero-sub{left:0;top:122px;width:940px;padding-left:160px;text-align:center;color:var(--white);font-size:11.5px;line-height:22px}
.hero-arrow{top:195px;width:40px;height:40px;border-radius:50%;background:rgba(255,255,255,.45)}
.hero-arrow svg{display:block}
.search{left:131px;top:575px;width:940px;height:103px;background:linear-gradient(#fff,#e1e1e1)}
.search-label{left:21px;top:35px;font-family:"PT Serif",Georgia,serif;font-style:italic;font-weight:700;font-size:24px;color:var(--navy)}
.search-input{left:301px;top:32px;width:480px;height:40px;background:var(--white);border:1px solid #cfcfcf;font-size:11px;font-style:italic;color:#999;padding:12px 14px}
.search-btn{left:805px;top:34px;width:119px;height:38px;background:var(--blue-bright);color:var(--white);font-size:14px;text-align:center;line-height:38px}

/* section headings */
.heading{left:0;width:1200px;text-align:center;color:var(--blue);font-size:21px;font-weight:400}
.lead{left:140px;width:920px;text-align:center;color:var(--muted);font-size:11.5px;line-height:22px}

/* pricing */
.plan{width:215px;background:linear-gradient(90deg,#cfcfcf,#e6e6e6 50%,#cfcfcf)}
.plan-name{height:28px;background:var(--black);color:var(--white);text-align:center;font-size:18px;line-height:28px;font-family:Arimo,Arial,sans-serif}
.plan-price{height:95px;background:linear-gradient(#0e3d8e,#1d64c9 60%,#1f5cb8);color:var(--white);font-family:Arimo,Arial,sans-serif;padding:18px 0 0 40px}
.plan-price sup{font-size:28px;vertical-align:28px}
.plan-price b{font-size:64px;font-weight:400;letter-spacing:-2px}
.plan-price small{font-size:26px}
.plan ul{list-style:none;padding:22px 0 0 20px}
.plan li{font-size:12.5px;font-weight:600;height:42.5px;color:var(--ink)}
.plan li::before{content:">";display:inline-block;width:24px;color:#888;font-weight:400;font-size:11px}
.cart{position:absolute;left:20px;bottom:10px;width:178px;height:30px;border-radius:4px;background:linear-gradient(#3a3a3a,#121212);color:var(--white);font-size:13px;line-height:30px;padding-left:42px}
.cart::after{content:"»";position:absolute;right:0;top:0;width:40px;height:30px;border-radius:0 4px 4px 0;background:var(--blue-bright);text-align:center;font-size:20px;line-height:28px}
.plan.featured{background:linear-gradient(90deg,#0b2f72,#1c5fc2 50%,#0b2f72)}
.plan.featured .plan-name{height:38px;line-height:38px;background:linear-gradient(#333,#111)}
.plan.featured .plan-price{background:linear-gradient(#3a3a3a,#151515);height:90px}
.plan.featured li{color:#111}
.plan.featured li::before{content:"▸";color:var(--white)}
.plan.featured .cart{background:linear-gradient(#bbb,#777);color:#eee}

/* premium band */
.band{left:0;top:1398px;width:1200px;height:351px;background:var(--band)}
.band-price{left:0;top:41px;width:1200px;text-align:center;color:var(--blue);font-size:16px}
.server{left:177px;top:133px;width:213px;height:172px;background:linear-gradient(90deg,#101010,#2a3a55 30%,#0b0b0b 50%,#2a3a55 70%,#111);clip-path:polygon(0 12%,100% 12%,100% 100%,0 100%)}
.plan-title{left:643px;top:140px;color:var(--blue);font-size:15px}
.ticks{list-style:none;font-size:12px;color:#555}
.ticks li{height:33px;padding-left:28px;position:relative}
.ticks li::before{content:"";position:absolute;left:2px;top:4px;width:7px;height:7px;border-right:2px solid var(--navy);border-bottom:2px solid var(--navy);transform:rotate(-45deg)}

/* free services */
.service{left:133px}
.service h3{font-size:15px;font-weight:400;color:var(--blue);padding-left:37px;position:relative;line-height:22px}
.service h3::before{content:"";position:absolute;left:0;top:1px;width:21px;height:21px;border-radius:50%;background:var(--navy)}
.service h3::after{content:"";position:absolute;left:6px;top:8px;width:6px;height:6px;border-right:2px solid #fff;border-bottom:2px solid #fff;transform:rotate(-45deg)}
.service p{font-size:11.5px;color:var(--muted);margin-top:8px}
.feature-icon{width:52px;height:44px;border-radius:4px}
.feature-title{font-size:15px;color:var(--blue)}
.feature-text{width:290px;font-size:11px;color:var(--muted);line-height:23px}

/* about */
.award{left:160px;top:2221px;width:132px;height:232px;background:linear-gradient(#c4c4c4 0%,#9a9eaa 45%,#1f2c63 100%)}
.about{left:380px;width:720px;font-size:11.5px;color:var(--muted);line-height:23px}

/* footer */
.footer{left:0;top:2474px;width:1200px;height:181px;background:var(--dark)}
.footer .social{position:absolute;left:505px;top:21px}
.footer-links{left:0;top:83px;width:1200px;text-align:center;color:var(--white);font-size:12px;word-spacing:2px}
.copyright{left:0;top:131px;width:1200px;text-align:center;color:var(--white);font-size:11px}
</style>
</head>
<body>

<header>
  <div class="abs topbar">
    <nav class="abs topnav">
      <span>Company</span><span>Partners</span><span>Support</span><span>Contact Us</span><span>Shopping Cart</span><span>References</span><span>Pricing</span>
    </nav>
    <div class="social" aria-label="Social links"><i></i><i></i><i></i><i></i><i></i></div>
  </div>
  <div class="abs brand">quendix</div>
  <nav class="abs mainnav">
    <span>Home</span><span>Domain Name Center</span><span>Web Site Hosting Center</span><span>S.E.O.Toolkit</span><span>Support</span><span>Client Area</span>
  </nav>
</header>

<section class="abs hero" role="img" aria-label="Photo of a business team meeting around a table with a laptop and a wall screen showing a bar chart">
  <h1 class="abs hero-title">Our Bussiness is Built ti Serve Yours</h1>
  <p class="abs hero-sub">Included free with every hosting plan, Quendix's premium Site-<br>Builder lets anyone easily create a business</p>
  <div class="abs hero-arrow" style="left:17px"><svg width="40" height="40"><path d="M23 12 15 20 23 28" fill="none" stroke="#fff" stroke-width="3"/></svg></div>
  <div class="abs hero-arrow" style="left:880px"><svg width="40" height="40"><path d="M17 12 25 20 17 28" fill="none" stroke="#fff" stroke-width="3"/></svg></div>
</section>
<form class="abs search">
  <label class="abs search-label">Find Your Domain Name:</label>
  <div class="abs search-input">Enter a domain name:</div>
  <div class="abs search-btn">SEARCH</div>
</form>

<h2 class="abs heading" style="top:720px">Choose a Hosting Package</h2>
<p class="abs lead" style="top:764px">Registering a domain is the first step in building your website. Choose from dozens of domain extensions such as .com, .net, .us, .tel, .biz, .org, .ca and .us. Quendix offers competitive prices, easy domain search and registration, auto-renewal and domain transfers.</p>

<div class="abs plan" style="left:149px;top:855px;height:432px">
  <div class="plan-name">Basic</div>
  <div class="plan-price"><sup>$</sup><b>10</b><small>/MO</small></div>
  <ul><li>5 Websites Cap</li><li>1TB Bandwidth Cap</li><li>60GB Space Storage</li><li>Domain Name Included</li></ul>
  <div class="cart">Add to Cart</div>
</div>
<div class="abs plan" style="left:382px;top:855px;height:432px">
  <div class="plan-name">Professional</div>
  <div class="plan-price"><sup>$</sup><b>12</b><small>/MO</small></div>
  <ul><li>10 Websites Cap</li><li>5TB Bandwidth Cap</li><li>80GB Space Storage</li><li>Domain Name Included</li><li>24/7 Unlimited Support</li></ul>
  <div class="cart">Add to Cart</div>
</div>
<div class="abs plan featured" style="left:609px;top:844px;height:453px">
  <div class="plan-name">Business</div>
  <div class="plan-price"><sup>$</sup><b>16</b><small>/MO</small></div>
  <ul><li>15 Websites Cap</li><li>10TB Bandwidth Cap</li><li>100GB Space Storage</li><li>Domain Name Included</li><li>24/7 Unlimited Support</li><li>Custom E-Mail</li></ul>
  <div class="cart" style="bottom:20px">Add to Cart</div>
</div>
<div class="abs plan" style="left:834px;top:855px;height:432px">
  <div class="plan-name">Enterprise</div>
  <div class="plan-price"><sup>$</sup><b>20</b><small>/MO</small></div>
  <ul><li>20 Websites Cap</li><li>50TB Bandwidth Cap</li><li>200GB Space Storage</li><li>Domain Name Included</li><li>24/7 Unlimited Support</li><li>Custom E-Mail</li></ul>
  <div class="cart">Add to Cart</div>
</div>

<h2 class="abs heading" style="top:1344px">Premium Business Hosting</h2>
<section class="abs band">
  <p class="abs band-price">From $ 90 / Years</p>
  <p class="abs lead" style="top:70px">Included free with every hosting plan, Quendix's premium SiteBuilder lets anyone easily create a business-quality website......</p>
  <div class="abs server" role="img" aria-label="Illustration of three black server towers with glowing blue stripes"></div>
  <p class="abs plan-title">Quendix's e-Lite Plan :</p>
  <ul class="abs ticks" style="left:540px;top:200px"><li>Domain Name</li><li>100 Mb Space</li><li>5 GB Transfer</li></ul>
  <ul class="abs ticks" style="left:758px;top:200px"><li>Unlimited Email Accounts</li><li>Unlimited Aliases</li><li>Dedicated Support</li></ul>
</section>

<h2 class="abs heading" style="top:1774px">Get These Free services With all &nbsp;Accounts</h2>
<div class="abs service" style="top:1836px"><h3>Secure Your Domain Name</h3><p>Register,Renew,transfer or Search Your Domain Name</p></div>
<div class="abs service" style="top:1907px"><h3>Effective Website Development</h3><p>Register,Renew,transfer or Search Your Domain Name</p></div>
<div class="abs service" style="top:1978px"><h3>Web Site Hosting</h3><p>Register,Renew,transfer or Search Your Domain Name</p></div>
<div class="abs service" style="top:2048px"><h3>Market Your Web Site</h3><p>Register,Renew,transfer or Search Your Domain Name</p></div>

<div class="abs feature-icon" style="left:504px;top:1843px;background:linear-gradient(#e3c276,#b98b35)" role="img" aria-label="Envelope icon"></div>
<p class="abs feature-title" style="left:577px;top:1853px">Easy Transfer</p>
<p class="abs feature-text" style="left:504px;top:1897px">As an Domora-accredited registrar for more than 10 years, Quendix is a leading provider of domain email medium-sized businesses.....</p>
<div class="abs feature-icon" style="left:818px;top:1833px;background:linear-gradient(#f2f2f2,#b7b7b7);border-radius:50%;width:48px;height:52px" role="img" aria-label="Stopwatch icon"></div>
<p class="abs feature-title" style="left:887px;top:1853px">Site Builder</p>
<p class="abs feature-text" style="left:814px;top:1897px">As an Domora-accredited registrar for more than 10 years, Quendix is a leading provider of domain email medium-sized businesses.....</p>
<div class="abs feature-icon" style="left:504px;top:1992px;background:linear-gradient(#eef2f7,#9fb2c9)" role="img" aria-label="Installer window icon"></div>
<p class="abs feature-title" style="left:577px;top:2003px">Setuplane</p>
<p class="abs feature-text" style="left:504px;top:2047px">As an Domora-accredited registrar for more than 10 years, Quendix is a leading provider of domain email medium-sized businesses.....</p>
<div class="abs feature-icon" style="left:814px;top:1994px;background:linear-gradient(#b8de6a,#6d9e24)" role="img" aria-label="Paper plane icon"></div>
<p class="abs feature-title" style="left:887px;top:2003px">Be Found</p>
<p class="abs feature-text" style="left:814px;top:2047px">As an Domora-accredited registrar for more than 10 years, Quendix is a leading provider of domain email medium-sized businesses.....</p>

<h2 class="abs heading" style="top:2172px">Quendix Makes it Easy To Get Online</h2>
<div class="abs award" role="img" aria-label="Award badge placeholder: silver rosette with navy ribbon"></div>
<p class="abs about" style="top:2245px">Quendix's website hosting plans are fast, flexible and affordable. We offer plans to meet your varying bandwidth and disk space requirements. All web hosting plans include free setup, one-click install web applications, and SiteBuilder, our do-it-yourself website building tool. Create a strong online web presence with Quendix hosting.</p>
<p class="abs about" style="top:2350px">As an award winning, premium provider of Internet services for small businesses and individuals, Quendix offers best in class products, dedicated customer support and the highest service reliability available. Choose Quendix and start building you website today.........</p>

<footer class="abs footer">
  <div class="social" aria-label="Social links"><i></i><i></i><i></i><i></i><i></i></div>
  <p class="abs footer-links">Home &nbsp; / &nbsp; Domain Name Center &nbsp; / &nbsp; Web Site Hosting Center &nbsp; / &nbsp; S.E.O.Toolkit &nbsp; / &nbsp; Support &nbsp; / &nbsp; Client Area</p>
  <p class="abs copyright">Copyright 2014 Quendix.All Right Reseved.</p>
</footer>

</body>
</html>
```